Quillmere Business Card

I have a current card that I like it just needs a couple little changes to make it perfect. I would like the font size bigger so it could be easily read by older customers.

Business

```html
<!DOCTYPE html>
<html lang="en">
<head>
<meta charset="utf-8">
<title>Quillmere Business Card</title>
<link href="https://fonts.googleapis.com/css2?family=Questrial&display=swap" rel="stylesheet">
<style>
  :root {
    --bg: #5a5a5a;
    --card-black: #050505;
    --card-green: #79b77a;
    --brand-green: #3fb93f;
    --white: #ffffff;
    --ink: #0a0a0a;
    --paper: #f6f6f4;
    --sun: #f2e84a;
  }
  * { margin: 0; padding: 0; box-sizing: border-box; }
  html, body { width: 1200px; height: 1000px; overflow: hidden; }
  body {
    background: var(--bg);
    font-family: "Questrial", "Century Gothic", sans-serif;
    display: flex; flex-direction: column; align-items: center; justify-content: center; gap: 50px;
  }
  .card {
    width: 760px; height: 434px; position: relative; overflow: hidden;
    box-shadow: 0 8px 24px rgba(0,0,0,.35);
  }
  .card--front {
    background: linear-gradient(to bottom, var(--card-black) 0%, var(--card-black) 35%, #2d5a2e 62%, var(--card-green) 100%);
  }
  .business-name {
    position: absolute; left: 30px; top: 26px;
    color: var(--brand-green); font-size: 40px; font-weight: 700; letter-spacing: .5px;
  }
  .website {
    position: absolute; right: 30px; top: 84px;
    color: var(--white); font-size: 27px;
  }
  .brand-mark {
    position: absolute; left: 34px; top: 150px;
    display: flex; align-items: center; gap: 12px;
    color: var(--white); font-size: 30px; font-weight: 700;
  }
  .brand-mark .dot { width: 22px; height: 22px; border-radius: 50%; background: var(--white); }
  .season-icons { position: absolute; right: 40px; top: 130px; }
  .tagline {
    position: absolute; right: 32px; top: 198px;
    color: var(--brand-green); font-size: 22px; letter-spacing: 5px;
  }
  .person {
    position: absolute; right: 30px; top: 236px;
    color: var(--white); font-size: 36px; font-weight: 700;
  }
  .email {
    position: absolute; right: 30px; top: 282px;
    color: var(--white); font-size: 25px; font-weight: 700;
  }
  .phone-line {
    position: absolute; left: 30px; top: 322px;
    display: flex; align-items: center; gap: 8px;
    color: var(--ink); font-size: 27px; font-weight: 700; letter-spacing: 1.5px;
  }
  .address {
    position: absolute; left: 30px; top: 366px;
    color: var(--ink); font-size: 27px; font-weight: 700; letter-spacing: 1.5px;
  }
  .card--back { background: var(--paper); }
  .services {
    position: absolute; right: 34px; top: 30px; text-align: right;
    color: var(--brand-green); font-size: 25px; font-weight: 700; line-height: 1.15;
  }
  .hours {
    position: absolute; left: 30px; bottom: 36px;
    color: var(--ink); font-size: 15px; font-weight: 700;
  }
</style>
</head>
<body>
  <section class="card card--front">
    <h1 class="business-name">Quillmere Motorsports and Marine</h1>
    <p class="website">www.quillmeremotorsports.com</p>
    <div class="brand-mark"><span class="dot"></span><span>Quillmere</span></div>
    <svg class="season-icons" width="270" height="60" viewBox="0 0 270 60" role="img" aria-label="Four season icons: leaf, water drop, snowflake and sun">
      <rect x="4" y="6" width="48" height="48" rx="10" fill="#ffffff"/>
      <path d="M96 6 C96 6 76 30 76 40 a20 20 0 0 0 40 0 C116 30 96 6 96 6 Z" fill="#ffffff"/>
      <rect x="146" y="6" width="48" height="48" rx="10" fill="#ffffff"/>
      <circle cx="242" cy="30" r="24" fill="#ffffff"/>
      <circle cx="242" cy="30" r="15" fill="var(--sun)"/>
    </svg>
    <p class="tagline">Fun for all seasons</p>
    <p class="person">Dale Hendricks</p>
    <p class="email">dale@quillmeremotorsports.com</p>
    <p class="phone-line">
      <svg width="22" height="22" viewBox="0 0 24 24" aria-hidden="true"><path d="M6.6 10.8a15 15 0 0 0 6.6 6.6l2.2-2.2a1 1 0 0 1 1-.25 11 11 0 0 0 3.6.6 1 1 0 0 1 1 1V20a1 1 0 0 1-1 1A17 17 0 0 1 3 4a1 1 0 0 1 1-1h3.5a1 1 0 0 1 1 1 11 11 0 0 0 .6 3.6 1 1 0 0 1-.25 1z" fill="#0a0a0a"/></svg>
      555-014-2210 Fax: 555-014-2277
    </p>
    <p class="address">2840 Harbor Road West, Millbrook, MN 55990</p>
  </section>

  <section class="card card--back">
    <p class="services">Servicing all makes and models of boats,<br>snowmobiles, motorcycles and ATVs.<br>Custom welding available for aluminium and steel.</p>
    <p class="hours">Hours: Mon – Wed 9am – 5:30pm • Thurs 9am – 7pm • Fri 9am – 5:30pm • Sat 9am – 3:30pm</p>
  </section>
</body>
</html>
```